Mental Health & Addiction Podcast Art

Project: Podcast Cover Art / Visual Identity
Podcast Name: The Mending Path
Focus: Recovery from substance use and mental health
Objectives
Create compelling podcast artwork that:
Reflects the themes of hope, healing, and personal growth
Establishes credibility and professionalism
Appeals to individuals seeking recovery resources and support
Maintains strong brand consistency with Larkspur Wellness
Brand Integration Requirements
Logo incorporation: Integrate an element from the Larkspur Wellness Logo—potentially an abstract or partial use of the sun motif
Flexibility: Open to creative interpretations (e.g., sun rays as background texture, sunrise gradient, partial sun as a design accent)
Mandatory: Must adhere to existing Larkspur Wellness brand guidelines (approved color palette, typography, and visual style)

Target Market(s)

United states, people with addiction and mental health disorders.

Industry/Entity Type

Wellness

Font styles to use
Other font styles liked:
• See Brand Guide

Requirements
Must have
• Match brand guide, in corporate elements of the Larkspur Wellness Logo icon

```html
<!DOCTYPE html>
<html lang="en">
<head>
<meta charset="utf-8">
<title>The Mending Path — Podcast Cover</title>
<link href="https://fonts.googleapis.com/css2?family=Source+Serif+4:opsz,wght@8..60,700&display=swap" rel="stylesheet">
<style>
  :root {
    --page: #d6d6d6;
    --sky-top: #455d70;
    --sky-mid: #8c989e;
    --haze: #dcc7a2;
    --glow: #f6a41c;
    --ridge: #5a2a14;
    --earth: #120808;
    --brand-gold: #f5a800;
    --ink-light: #ffffff;
  }
  html, body {
    margin: 0;
    width: 1200px;
    height: 900px;
    overflow: hidden;
    background: var(--page);
  }
  .cover {
    position: absolute;
    left: 270px;
    top: 120px;
    width: 660px;
    height: 660px;
    overflow: hidden;
    font-family: "Source Serif 4", Georgia, serif;
    font-weight: 700;
  }
  .cover__scene {
    position: absolute;
    inset: 0;
    background:
      radial-gradient(ellipse 90px 50px at 50% 58%, rgba(255,240,190,0.95), rgba(255,200,80,0) 100%),
      linear-gradient(to bottom,
        var(--sky-top) 0%,
        var(--sky-mid) 30%,
        var(--haze) 48%,
        var(--glow) 57%,
        var(--ridge) 64%,
        #2a1210 74%,
        var(--earth) 100%);
  }
  .cover__brand {
    position: absolute;
    top: 98px;
    right: 34px;
    display: flex;
    align-items: center;
    gap: 8px;
    color: var(--ink-light);
    font-size: 17px;
    letter-spacing: 0.02em;
  }
  .cover__brand-dot {
    width: 12px;
    height: 12px;
    border-radius: 50%;
    background: var(--brand-gold);
  }
  .cover__title {
    position: absolute;
    left: 46px;
    top: 390px;
    margin: 0;
    letter-spacing: -0.02em;
  }
  .cover__title-lead {
    display: block;
    color: var(--brand-gold);
    font-size: 58px;
    line-height: 0.84;
    margin-bottom: 12px;
  }
  .cover__title-main {
    display: block;
    color: var(--ink-light);
    font-size: 94px;
    line-height: 0.9;
  }
  .cover__rule {
    position: absolute;
    right: 40px;
    bottom: 54px;
    width: 40px;
    height: 2px;
    background: var(--brand-gold);
  }
</style>
</head>
<body>
  <main class="cover">
    <div class="cover__scene" role="img" aria-label="Photograph of a sunrise over layered desert mountain ridges"></div>

    <div class="cover__brand">
      <span class="cover__brand-dot"></span>
      <span class="cover__brand-name">Larkspur Wellness</span>
    </div>

    <h1 class="cover__title">
      <span class="cover__title-lead">The</span>
      <span class="cover__title-main">Mending</span>
      <span class="cover__title-main">Path</span>
    </h1>

    <div class="cover__rule" aria-hidden="true"></div>
  </main>
</body>
</html>
```